New website for selling opensource software business to business

Website K7 Software

The open source software industry has grown enormously in recent years. More and more customers from software companies choose an open source solution. K7 Software is going to fulfill this increasing demand.

Core business

Reselling software subcriptions (business to business).

Side business

Selling consultancy and Training to customers

Goals:

- Binding of customers to K7 IT Group
- Sales of subscriptions to customer
- Enlarge network K7 IT Group
- USP: Sales of complete package, Software, consultancy and training

Products

There are a couple of products/ services that K7 will provide. Below you will find an overview of the Products:

- Bluefen subscriptions
- Cratel subscriptions
- Velmor products
- Customized consultancy for the customer
- Customized training for the customer

Style

Behind the website should be a cms system like wordpress.

Target Market(s)

Business - Business

Industry/Entity Type

Business

Coding

Coded - Design and coding required

Number of Pages Required

5+ page

Font styles to use
Other font styles liked:
• Calibri

Colors
0355a3
3176b5
85abd2

Requirements
Must have
• Home page with large photo background, About us, contact page with safe option to request more info
• Portfolio pages:
• 4 pages with a product group each:
• 1. Blue fen
• 2. Crates
• 3. Velmor
• 4. Trustwardly
• 1. Blue Fen
• On top space for short info/bullets about Blue fen. Further, a grid with 8 columns. In the columns 2 buttons both lead to a popup. A popup for information and a popup for requesting a quote.
• 2. Cratel:
• On top space for short info/bullets about Cratel. Further, a grid with 3 columns. In the columns 2 buttons both lead to a popup. A popup for information and a popup for requesting a quote.
• 1. Velmor:
• On top space for short info/bullets about Velmor. Further, a grid with 4 columns. In the columns 2 buttons both lead to a popup. A popup for information and a popup for requesting a quote.
• 2. Trustwardly:
• On top space for short info/bullets about Trustwardly. Further, a grid with 2 columns. In the columns 2 buttons both lead to a popup. A popup for information and a popup for requesting a quote.

```html
<!DOCTYPE html>
<html lang="en">
<head>
<meta charset="utf-8">
<title>K7 Software</title>
<link href="https://fonts.googleapis.com/css2?family=Poppins:wght@400;500;600&family=Open+Sans:ital,wght@0,400;0,600;1,400&display=swap" rel="stylesheet">
<style>
:root{
  --blue:#0355a3;
  --blue-mid:#3176b5;
  --blue-light:#85abd2;
  --purple:#4a2b8c;
  --ink:#1f2328;
  --text:#5b6470;
  --muted:#8a929c;
  --soft:#f2f5f7;
  --line:#e3e6ea;
  --footer:#27313c;
  --white:#ffffff;
}
*{margin:0;padding:0;box-sizing:border-box}
html,body{width:1200px;height:3371px;overflow:hidden}
body{position:relative;background:var(--white);font-family:"Open Sans",Arial,sans-serif;color:var(--text)}
.abs{position:absolute}
h1,h2,h3,h4,.nav,.btn{font-family:"Poppins",Arial,sans-serif}

/* header */
.site-header{position:absolute;left:0;top:0;width:1200px;height:80px;background:var(--white);z-index:3}
.brand{position:absolute;left:88px;top:12px;display:flex;align-items:center;gap:8px}
.brand-mark{width:56px;height:56px;border-radius:50%;background:#fff;box-shadow:0 2px 8px rgba(0,0,0,.18);display:flex;align-items:center;justify-content:center;font-family:"Poppins",sans-serif;font-weight:600;font-size:13px;color:var(--blue)}
.nav{position:absolute;top:0;left:600px;height:80px;display:flex;align-items:center;gap:34px;font-size:13px;color:var(--ink)}
.nav a{text-decoration:none;color:inherit;position:relative;height:80px;display:flex;align-items:center}
.nav a.active{color:var(--blue-mid)}
.nav a.active::before{content:"";position:absolute;top:0;left:-4px;right:-4px;height:4px;background:var(--blue-mid)}
.btn-request{position:absolute;left:946px;top:20px;width:166px;height:40px;background:var(--purple);color:#fff;font-size:11px;font-weight:500;display:flex;align-items:center;justify-content:center;letter-spacing:.2px}

/* hero */
.hero{position:absolute;left:0;top:80px;width:1200px;height:590px;background:linear-gradient(100deg,#7a3b2c 0%,#b5654d 30%,#8f5a4a 55%,#c9a48f 80%,#e6d6c8 100%)}
.hero-shade{position:absolute;inset:0;background:rgba(40,20,15,.35)}
.hero-curve{position:absolute;left:0;top:620px;width:1200px;height:60px}
.hero h1{position:absolute;left:0;width:1200px;top:295px;text-align:center;color:#fff;font-weight:600;font-size:36px;line-height:47px}
.btn-outline-white{position:absolute;left:527px;top:410px;width:146px;height:40px;border:2px solid #fff;color:#fff;font-size:10px;font-weight:500;display:flex;align-items:center;justify-content:center}
.mouse{position:absolute;left:590px;top:598px;width:20px;height:32px;border:2px solid #fff;border-radius:10px}
.mouse::after{content:"";position:absolute;left:7px;top:6px;width:2px;height:6px;background:#fff;border-radius:1px}
.hero-dots{position:absolute;left:1151px;top:350px;display:flex;flex-direction:column;gap:12px}
.hero-dots span{width:8px;height:8px;border-radius:50%;background:rgba(255,255,255,.5)}
.hero-dots span:first-child{background:#fff}

/* partners */
.partners{position:absolute;top:728px;left:0;width:1200px;height:40px}
.partner{position:absolute;top:0;height:40px;display:flex;align-items:center;gap:8px;font-family:"Poppins",sans-serif;font-weight:500;font-size:22px;color:#9aa0a6}
.partner .dot{width:26px;height:26px;border-radius:50%;background:#c5c9cd}
.divider{position:absolute;left:90px;top:828px;width:1020px;height:1px;background:var(--line)}

/* about */
.photo-circle{position:absolute;border-radius:50%}
.about-title{position:absolute;left:650px;top:955px;font-size:28px;font-weight:500;line-height:33px;color:var(--ink)}
.rule{position:absolute;height:2px;width:40px;background:var(--line)}
.about-text{position:absolute;left:650px;top:1062px;width:390px;font-size:12.5px;line-height:24px;color:var(--text)}
.btn{position:absolute;height:40px;font-size:11px;font-weight:500;display:flex;align-items:center;justify-content:center}
.btn-blue{background:var(--blue);color:#fff}
.btn-line{border:2px solid var(--ink);color:var(--ink)}

/* provide */
.provide{position:absolute;left:0;top:1395px;width:1200px;height:498px;background:var(--soft)}
.section-title{position:absolute;left:0;width:1200px;text-align:center;font-size:28px;font-weight:500;color:var(--ink)}
.card{position:absolute;top:1557px;width:502px;height:250px;color:#fff}
.card.purple{left:90px;background:linear-gradient(90deg,#4b2a90,#5d3aa6 60%,#6a4bb0)}
.card.blue{left:609px;background:linear-gradient(90deg,#1565b8,#2a7cc8 60%,#3b8bd0)}
.card-shadow{position:absolute;left:130px;top:1760px;width:420px;height:80px;background:rgba(60,40,120,.25);filter:blur(18px)}
.card h3{position:absolute;left:38px;top:70px;font-size:16px;font-weight:600;line-height:24px}
.card p{position:absolute;left:38px;top:132px;width:260px;font-size:12px;line-height:26px}
.card .btn{top:105px;width:130px;font-size:10px}
.btn-white{background:#fff;color:var(--ink)}
.btn-ghost{border:2px solid #fff;color:#fff}

/* activities */
.activity{position:absolute;top:2071px;width:300px;text-align:center}
.activity .icon{width:86px;height:86px;border-radius:50%;border:1px solid var(--line);margin:0 auto;display:flex;align-items:center;justify-content:center;background:#fff}
.activity h4{margin-top:28px;font-size:16px;font-weight:500;color:var(--ink)}

/* testimonials */
.testimonials{position:absolute;left:0;top:2293px;width:1200px;height:490px;background:radial-gradient(ellipse at center,#ffffff 0%,#f3f4f5 55%,#e2e4e6 100%)}
.avatar{position:absolute;border-radius:50%;border:3px solid #fff;box-shadow:0 2px 6px rgba(0,0,0,.2);background:linear-gradient(135deg,#c9a98f,#7d6a5e)}
.quote-mark{position:absolute;left:0;width:1200px;top:2498px;text-align:center;font-family:"Poppins",sans-serif;font-size:54px;line-height:54px;color:var(--ink);font-weight:600}
.quote{position:absolute;left:300px;width:600px;top:2556px;text-align:center;font-style:italic;font-size:12.5px;line-height:27px;color:var(--muted)}
.quote-name{position:absolute;left:0;width:1200px;top:2617px;text-align:center;font-size:15px;color:var(--ink)}
.slider-dots{position:absolute;left:580px;top:2686px;display:flex;gap:8px}
.slider-dots span{width:7px;height:7px;border-radius:50%;background:var(--blue-light)}
.slider-dots span:first-child{background:var(--blue)}

/* footer */
.site-footer{position:absolute;left:0;top:2783px;width:1200px;height:588px;background:linear-gradient(180deg,#34404c,#222b35)}
.cta-title{position:absolute;left:0;width:1200px;top:2860px;text-align:center;color:#fff;font-size:22px;font-weight:500}
.cta-sub{position:absolute;left:0;width:1200px;top:2904px;text-align:center;color:#fff;font-size:12px}
.foot-logo{position:absolute;left:140px;top:3065px;width:80px;height:80px;border-radius:50%;background:#fff;display:flex;align-items:center;justify-content:center;font-family:"Poppins",sans-serif;font-weight:600;font-size:14px;color:var(--blue);text-align:center;line-height:16px}
.social{position:absolute;top:3159px;width:32px;height:32px;border-radius:50%;background:var(--blue-mid)}
.foot-col{position:absolute;top:3060px;color:#fff}
.foot-col h4{font-size:14px;font-weight:500;margin-bottom:22px}
.foot-col li{list-style:none;font-size:12px;line-height:31.5px;color:#cfd5db}
.contact-line{display:flex;align-items:center;gap:10px;font-size:12px;line-height:31.5px;color:#fff}
.copyright{position:absolute;left:0;width:1200px;top:3334px;text-align:center;color:#fff;font-size:11.5px}
.to-top{position:absolute;left:1131px;top:3294px;width:44px;height:44px;border-radius:50%;background:#fff;display:flex;align-items:center;justify-content:center}
</style>
</head>
<body>

<header class="site-header">
  <div class="brand"><div class="brand-mark">K7</div></div>
  <nav class="nav">
    <a class="active">Home</a>
    <a>About us</a>
    <a>Portfolio &#709;</a>
    <a>Contact</a>
  </nav>
  <div class="btn-request">REQUEST INFORMATION</div>
</header>

<section class="hero" role="img" aria-label="Photo of a team working together at a laptop in a bright office">
  <div class="hero-shade"></div>
</section>
<svg class="hero-curve" viewBox="0 0 1200 60" preserveAspectRatio="none" aria-hidden="true">
  <path d="M0 10 Q600 90 1200 10 L1200 60 L0 60 Z" fill="#ffffff"/>
</svg>
<h1 class="abs" style="left:0;width:1200px;top:295px;text-align:center;color:#fff;font-weight:600;font-size:36px;line-height:47px">We are K7 Software<br>We provide open source solutions</h1>
<div class="btn-outline-white">VIEW SOLUTIONS</div>
<div class="mouse"></div>
<div class="hero-dots"><span></span><span></span><span></span></div>

<div class="partners">
  <div class="partner" style="left:300px"><span class="dot"></span>Cratel</div>
  <div class="partner" style="left:484px;color:#333"><span class="dot" style="background:#b33"></span>Bluefen</div>
  <div class="partner" style="left:654px">Velmor</div>
  <div class="partner" style="left:846px;font-size:16px"><span class="dot" style="width:34px;height:34px"></span>K7</div>
</div>
<div class="divider"></div>

<div class="photo-circle" style="left:150px;top:890px;width:420px;height:420px;background:linear-gradient(135deg,#d8c4a8,#9c7b5e 50%,#5a6b52);box-shadow:0 20px 40px rgba(0,0,0,.12)" role="img" aria-label="Photo of colleagues smiling around a table"></div>
<div class="photo-circle" style="left:84px;top:940px;width:112px;height:112px;border:4px solid #fff;background:linear-gradient(135deg,#a9b8c6,#5f7284)" role="img" aria-label="Photo of a man in an office"></div>
<div class="photo-circle" style="left:400px;top:1158px;width:170px;height:170px;border:5px solid #fff;background:linear-gradient(135deg,#e6e2dc,#8b4a58 60%,#2d5a4a);box-shadow:0 10px 24px rgba(0,0,0,.2)" role="img" aria-label="Photo of a group meeting"></div>

<h2 class="about-title">Some short intro<br>about us.</h2>
<div class="rule" style="left:650px;top:1037px"></div>
<p class="about-text">The open source software industry has grown enormously in recent years. More and more customers from software companies choose an open source solution. K7 Software is going to fulfill this increasing demand.</p>
<div class="btn btn-blue" style="left:650px;top:1185px;width:130px">LEARN MORE</div>
<div class="btn btn-line" style="left:793px;top:1185px;width:147px">VIEW PRODUCTS</div>

<section class="provide"></section>
<h2 class="section-title" style="top:1465px">We also provide</h2>
<div class="rule" style="left:580px;top:1513px"></div>
<div class="card-shadow"></div>
<div class="card purple" role="img" aria-label="Consultancy photo tinted purple">
  <h3>Customized consultancy<br>for customers.</h3>
  <p>Aenean commodo ligula eget dolor aenean massac um sociis natoque pen.</p>
  <div class="btn btn-white" style="left:328px">LEARN MORE</div>
</div>
<div class="card blue" role="img" aria-label="Training photo tinted blue">
  <h3>Customized training<br>for the customers.</h3>
  <p>Aenean commodo ligula eget dolor aenean massac um sociis natoque pen.</p>
  <div class="btn btn-ghost" style="left:329px">LEARN MORE</div>
</div>

<h2 class="section-title" style="top:1963px">Our key activities</h2>
<div class="rule" style="left:580px;top:2010px"></div>
<div class="activity" style="left:110px">
  <div class="icon"><svg width="34" height="38" viewBox="0 0 34 38" fill="none" stroke="#0355a3" stroke-width="1.6"><rect x="5" y="3" width="22" height="30" rx="2"/><path d="M10 12h12M10 18h12M10 24h8"/></svg></div>
  <h4>Sales of Software Licenses</h4>
</div>
<div class="activity" style="left:450px">
  <div class="icon"><svg width="40" height="36" viewBox="0 0 40 36" fill="none" stroke="#0355a3" stroke-width="1.6"><circle cx="10" cy="10" r="4"/><circle cx="20" cy="8" r="4"/><circle cx="30" cy="10" r="4"/><path d="M3 30v-8a7 7 0 0 1 14 0M13 30v-10a7 7 0 0 1 14 0v10M23 30v-8a7 7 0 0 1 14 0v8M2 31h36"/></svg></div>
  <h4>Providing Consultancy</h4>
</div>
<div class="activity" style="left:790px">
  <div class="icon"><svg width="38" height="36" viewBox="0 0 38 36" fill="none" stroke="#0355a3" stroke-width="1.6"><rect x="4" y="4" width="26" height="18"/><circle cx="26" cy="24" r="4"/><path d="M20 34a6 6 0 0 1 12 0M8 10h12M8 15h8"/></svg></div>
  <h4>Providing Training</h4>
</div>

<section class="testimonials" role="img" aria-label="Faded background photo of people at work"></section>
<div class="avatar" style="left:108px;top:2384px;width:36px;height:36px" role="img" aria-label="Client photo"></div>
<div class="avatar" style="left:-15px;top:2456px;width:44px;height:44px" role="img" aria-label="Client photo"></div>
<div class="avatar" style="left:85px;top:2485px;width:32px;height:32px" role="img" aria-label="Client photo"></div>
<div class="avatar" style="left:153px;top:2526px;width:40px;height:40px" role="img" aria-label="Client photo"></div>
<div class="avatar" style="left:6px;top:2579px;width:24px;height:24px" role="img" aria-label="Client photo"></div>
<div class="avatar" style="left:79px;top:2623px;width:48px;height:48px" role="img" aria-label="Client photo"></div>
<div class="avatar" style="left:1156px;top:2392px;width:24px;height:24px" role="img" aria-label="Client photo"></div>
<div class="avatar" style="left:991px;top:2451px;width:32px;height:32px" role="img" aria-label="Client photo"></div>
<div class="avatar" style="left:1081px;top:2494px;width:40px;height:40px" role="img" aria-label="Client photo"></div>
<div class="avatar" style="left:1158px;top:2486px;width:52px;height:52px" role="img" aria-label="Client photo"></div>
<div class="avatar" style="left:1010px;top:2601px;width:48px;height:48px" role="img" aria-label="Client photo"></div>
<div class="avatar" style="left:1126px;top:2607px;width:36px;height:36px" role="img" aria-label="Client photo"></div>
<h2 class="section-title" style="top:2408px;font-size:26px;line-height:32px">See what our clients<br>say about us</h2>
<div class="quote-mark">&ldquo;</div>
<p class="quote">"Enean leo ligula porttitor eu consequat vitae eleifend ac enim. Aliquam lorem ante dapibus in viverra quis feugiat a tellus phasellus viverra nulla ut metus varius"</p>
<div class="quote-name">-John Doe</div>
<div class="slider-dots"><span></span><span></span><span></span></div>

<footer class="site-footer" role="img" aria-label="Dark background photo of an office team"></footer>
<h2 class="cta-title">Have a project, get in touch with us</h2>
<p class="cta-sub">For consultation please call +123 456 7890 or schedule meeting below</p>
<div class="btn btn-blue" style="left:535px;top:2950px;width:130px">GET IN TOUCH</div>

<div class="foot-logo">K7</div>
<div class="social" style="left:90px" aria-label="Social one"></div>
<div class="social" style="left:139px" aria-label="Social two"></div>
<div class="social" style="left:187px" aria-label="Social three"></div>
<div class="social" style="left:235px" aria-label="Social four"></div>

<div class="foot-col" style="left:382px">
  <h4>Useful Links</h4>
  <ul><li>About</li><li>Team</li><li>How it works</li><li>FAQs</li><li>Career</li></ul>
</div>
<div class="foot-col" style="left:611px">
  <h4>Privacy &amp; Terms</h4>
  <ul><li>Privacy Policy</li><li>Terms &amp; Conditions</li><li>Disclaimer</li></ul>
</div>
<div class="foot-col" style="left:870px">
  <h4>Privacy &amp; Terms</h4>
  <div class="contact-line">We are here if you need us:</div>
  <div class="contact-line"><svg width="12" height="12" viewBox="0 0 24 24" fill="#3b8bd0"><path d="M6.6 10.8a15 15 0 0 0 6.6 6.6l2.2-2.2c.3-.3.7-.4 1-.2 1.1.4 2.3.6 3.6.6.6 0 1 .4 1 1V20c0 .6-.4 1-1 1A17 17 0 0 1 3 4c0-.6.4-1 1-1h3.5c.6 0 1 .4 1 1 0 1.3.2 2.5.6 3.6.1.3 0 .7-.2 1z"/></svg>0400 111 222</div>
  <div class="contact-line"><svg width="12" height="10" viewBox="0 0 24 18" fill="#3b8bd0"><path d="M0 0h24v18H0z"/><path d="M0 0l12 9 12-9" stroke="#27313c" stroke-width="2" fill="none"/></svg>info@k7software.example</div>
</div>

<p class="copyright">&copy; 2017, All Rights Reserved.</p>
<div class="to-top"><svg width="12" height="12" viewBox="0 0 12 12" fill="none" stroke="#1f2328" stroke-width="1.5"><path d="M6 11V1M2 5l4-4 4 4"/></svg></div>

</body>
</html>
```